a promotional poster design to promote our upcoming event. We want the date to be promoted as "Save the Date" for Sunday 4th July 2021.

Requirements
Must have
• the following text;

Save the Date! (stand out)
Sunday 4th July 2021 (stand out)
KTRB Family Mixed Netball Carnival
Nice to have
• make the date stand out. We want people to lock in the date we're promoting.

```html
<!DOCTYPE html>
<html lang="en">
<head>
<meta charset="utf-8">
<title>KTRB Family Mixed Netball Carnival – Save the Date</title>
<link rel="stylesheet" href="https://fonts.googleapis.com/css2?family=Barlow:wght@800&family=Fjalla+One&family=Righteous&display=swap">
<style>
  :root {
    --night: #050507;
    --band-purple: #2f3488;
    --band-sky: #1a74ba;
    --sun-yellow: #f1c42f;
    --date-blue: #1a72ba;
    --letter-light: #3fb0d6;
    --letter-mid: #2a8ec8;
    --letter-deep: #2d3390;
    --outline: #ffffff;
  }
  html, body {
    margin: 0;
    padding: 0;
    overflow: hidden;
    background: var(--night);
  }
  .poster {
    position: relative;
    width: 849px;
    height: 1200px;
    overflow: hidden;
    background: var(--night);
  }
  .fireworks {
    position: absolute;
    inset: 0;
    background:
      radial-gradient(circle at 130px 260px, rgba(120,200,170,.35), transparent 210px),
      radial-gradient(circle at 650px 310px, rgba(190,200,255,.35), transparent 190px),
      radial-gradient(circle at 80px 900px, rgba(200,110,140,.30), transparent 300px),
      radial-gradient(circle at 380px 1130px, rgba(90,190,190,.25), transparent 150px),
      var(--night);
  }
  .bands {
    position: absolute;
    inset: 0;
  }
  .event-title {
    position: absolute;
    left: 96px;
    top: 112px;
    margin: 0;
    font-family: "Fjalla One", sans-serif;
    font-weight: 400;
    font-size: 46px;
    color: var(--sun-yellow);
    transform: rotate(4.6deg);
    transform-origin: left top;
    white-space: nowrap;
    letter-spacing: -0.5px;
  }
  .partners {
    position: absolute;
    left: 540px;
    top: 52px;
    display: flex;
    gap: 22px;
    align-items: center;
    font-family: "Fjalla One", sans-serif;
    color: var(--sun-yellow);
    font-size: 15px;
    line-height: 1.1;
    text-align: center;
  }
  .partner {
    display: flex;
    align-items: center;
    gap: 6px;
  }
  .partner-dot {
    width: 12px;
    height: 12px;
    border-radius: 50%;
    background: var(--sun-yellow);
  }
  .headline {
    position: absolute;
    inset: 0;
    margin: 0;
    font-family: "Righteous", sans-serif;
    font-weight: 400;
  }
  .headline-line {
    position: absolute;
    display: block;
    line-height: 1;
    white-space: nowrap;
    background: linear-gradient(90deg, var(--letter-deep), var(--letter-mid) 25%, var(--letter-light) 50%, var(--letter-deep) 75%, var(--letter-mid));
    -webkit-background-clip: text;
    background-clip: text;
    color: transparent;
    -webkit-text-stroke: 3px var(--outline);
    filter: drop-shadow(-14px 12px 0 rgba(55,75,160,.55));
  }
  .line-save { left: 140px; top: 250px; font-size: 252px; letter-spacing: -14px; }
  .line-the  { left: 222px; top: 478px; font-size: 238px; letter-spacing: -12px; }
  .line-date { left: 100px; top: 688px; font-size: 258px; letter-spacing: -16px; }
  .event-date {
    position: absolute;
    left: 95px;
    top: 925px;
    margin: 0;
    font-family: "Barlow", sans-serif;
    font-weight: 800;
    font-size: 64px;
    color: var(--date-blue);
    transform: rotate(8.6deg);
    transform-origin: left top;
    white-space: nowrap;
    letter-spacing: 1px;
  }
</style>
</head>
<body>
  <main class="poster">
    <div class="fireworks" role="img" aria-label="Colourful fireworks and stars bursting across a black night sky"></div>

    <svg class="bands" width="849" height="1200" viewBox="0 0 849 1200" aria-hidden="true">
      <polygon points="0,0 849,78 849,118 810,228 0,175" fill="var(--band-purple)"/>
      <polygon points="565,21 849,74 849,112 450,114" fill="var(--band-sky)"/>
      <polygon points="140,882 849,994 849,1126 0,1044 0,1008" fill="var(--sun-yellow)"/>
    </svg>

    <div class="partners">
      <div class="partner"><span class="partner-dot"></span><span>Puff Free<br>Mob</span></div>
      <div class="partner"><span>Kinara Tribal<br>Health Service</span></div>
    </div>

    <h2 class="event-title">KTRB Family Mixed Netball Carnival</h2>

    <h1 class="headline">
      <span class="headline-line line-save">SAVE</span>
      <span class="headline-line line-the">THE</span>
      <span class="headline-line line-date">DATE!</span>
    </h1>

    <p class="event-date">Sunday 4th July 2021</p>
  </main>
</body>
</html>
```